Stationary Set Rebrand for Brenvik

We are a Canadian Distribution and Service Company that was established in 1969. Over the past 5 decades we have expanded our business and have warehouses across Canada. We specialize in adhesive tapes, adhesives, films, safety, warehouse, shipping, janitorial and packaging supplies.

We have updated our logo design and would like a new corporate branding identity that includes a new fresh Stationary Set (Business Cards, Letterhead, Letterhead MS Word, Envelope, Presentation Folders, Email Signatures, Notepad Covers, etc.)

Target Market(s)

Industrial Business Sector

Font styles to use
Sans Serif

Colors
0054AA
0677BA
7BADD7
CADEEF
E8F1F8
0094D4
00A9DD
6FCCEA
C7EBF8
E9F6FB
00AB8E
00BBA5
67D7C9
C6EFE9
E9F9F6
EB3D1F
EC4F4E
F09395
F8D3D4
FCEDEE

Requirements
Should not have
• Colors not too light, darker colours preferred

```html
<!DOCTYPE html>
<html lang="en">
<head>
<meta charset="utf-8">
<title>Brenvik Business Card</title>
<link href="https://fonts.googleapis.com/css2?family=Nunito:wght@400;600;800&display=swap" rel="stylesheet">
<style>
  :root {
    --bg: #9a9a9a;
    --card: #161616;
    --edge: #d1161b;
    --ink: #f2f2f2;
    --accent: #e0262b;
    --emboss: #3a3a3a;
  }
  * { box-sizing: border-box; margin: 0; padding: 0; }
  html, body {
    width: 1200px; height: 1083px; overflow: hidden;
    background: var(--bg);
    font-family: "Nunito", sans-serif;
  }
  .card {
    position: absolute; left: 300px;
    width: 600px; height: 343px;
    background: var(--card);
    border-bottom: 5px solid var(--edge);
    border-radius: 2px;
  }
  .card--front { top: 150px; }
  .card--back { top: 590px; }

  .wordmark {
    display: flex; align-items: center; gap: 10px;
    font-weight: 800; letter-spacing: -1px;
  }
  .wordmark__dot {
    width: 14px; height: 14px; border-radius: 50%;
    background: var(--accent);
  }
  .card--front .wordmark {
    position: absolute; left: 40px; top: 128px;
    font-size: 64px; color: var(--ink);
  }
  .divider {
    position: absolute; left: 345px; top: 70px;
    width: 1px; height: 200px; background: var(--ink);
  }
  .contact {
    position: absolute; left: 368px; top: 74px;
    color: var(--ink);
  }
  .contact__name { font-size: 19px; font-weight: 600; letter-spacing: 1px; }
  .contact__role { font-size: 13px; margin-top: 2px; }
  .contact__address { font-size: 13px; margin-top: 14px; line-height: 1.4; }
  .contact__list { list-style: none; margin-top: 12px; font-size: 13px; line-height: 1.55; }
  .contact__list li { display: flex; align-items: center; gap: 8px; }
  .contact__list svg { width: 12px; height: 12px; flex: none; }

  .card--back .wordmark {
    position: absolute; left: 0; right: 0; top: 100px;
    justify-content: center;
    font-size: 68px; color: var(--emboss);
  }
  .established {
    position: absolute; left: 0; right: 0; top: 250px;
    text-align: center; color: var(--ink); font-size: 15px;
  }
</style>
</head>
<body>
  <section class="card card--front">
    <div class="wordmark">Brenvik<span class="wordmark__dot"></span></div>
    <div class="divider"></div>
    <div class="contact">
      <p class="contact__name">DANIEL MERCER</p>
      <p class="contact__role">Development Manager Officer</p>
      <p class="contact__address">415 Harbor Line Road<br>Suite 210, Oakdale, ON 40218</p>
      <ul class="contact__list">
        <li>
          <svg viewBox="0 0 24 24" fill="var(--accent)"><path d="M6.6 10.8a15 15 0 0 0 6.6 6.6l2.2-2.2a1 1 0 0 1 1-.25 11.4 11.4 0 0 0 3.6.6 1 1 0 0 1 1 1V20a1 1 0 0 1-1 1A17 17 0 0 1 3 4a1 1 0 0 1 1-1h3.5a1 1 0 0 1 1 1c0 1.25.2 2.45.6 3.6a1 1 0 0 1-.25 1z"/></svg>
          555-014-2273
        </li>
        <li>
          <svg viewBox="0 0 24 24" fill="var(--accent)"><path d="M2 5h20v14H2z M2 5l10 8 10-8" stroke="var(--card)" stroke-width="1.5"/></svg>
          daniel.mercer@brenvikpack.com
        </li>
        <li>
          <svg viewBox="0 0 24 24" fill="none" stroke="var(--accent)" stroke-width="1.8"><circle cx="12" cy="12" r="9"/><path d="M3 12h18M12 3c3 3 3 15 0 18M12 3c-3 3-3 15 0 18"/></svg>
          brenvikpack.com
        </li>
      </ul>
    </div>
  </section>

  <section class="card card--back">
    <div class="wordmark">Brenvik<span class="wordmark__dot"></span></div>
    <p class="established">Estd. 1969</p>
  </section>
</body>
</html>
```